Evergold Fernbark Inc

Industry/Entity Type

Forestry

Contact Information for Business Card

Company name: Evergold Fernbark INC, Contact Info: Rovelio Marquin, Phone # 912 555 0187, Addres: 284 Willowbend Creek Rd, Glenwood GA 30428, Email: evergoldfernbark@mailbrook.net

```html
<!DOCTYPE html>
<html lang="en">
<head>
<meta charset="utf-8">
<title>Evergold Fernbark INC — Business Card</title>
<link href="https://fonts.googleapis.com/css2?family=Inter:wght@400;600;700&display=swap" rel="stylesheet">
<style>
  :root {
    --backdrop: #dcdcdc;
    --card-white: #ffffff;
    --brand-green: #0b6a0b;
    --green-dark: #005a00;
    --green-light: #0b8a0b;
    --text-grey: #5a5a5a;
    --wordmark-grey: #666666;
    --on-green: #ffffff;
    --mark-tint-front: #d6ead6;
    --mark-tint-back: rgba(255, 255, 255, 0.28);
  }
  * { box-sizing: border-box; margin: 0; padding: 0; }
  html, body {
    width: 1200px; height: 1200px; overflow: hidden;
    background: var(--backdrop);
    font-family: "Inter", sans-serif;
  }
  .canvas { position: relative; width: 1200px; height: 1200px; }
  .card {
    position: absolute; left: 262px; width: 686px; height: 392px;
    border-radius: 22px; overflow: hidden;
  }
  .card--front { top: 165px; background: var(--card-white); }
  .card--back {
    top: 653px;
    background: linear-gradient(35deg, var(--green-dark) 0%, #007200 50%, var(--green-light) 100%);
  }
  .wordmark {
    position: absolute; font-weight: 600; line-height: 34px; letter-spacing: -0.5px;
    font-size: 38px; white-space: nowrap;
  }
  .card--front .wordmark { left: 52px; top: 56px; color: var(--wordmark-grey); }
  .card--back .wordmark { left: 189px; top: 185px; color: var(--on-green); }
  .wordmark span { display: block; }
  .mark-area {
    position: absolute; border-radius: 6px;
  }
  .card--front .mark-area {
    left: 462px; top: 36px; width: 140px; height: 324px;
    background: var(--mark-tint-front);
  }
  .card--back .mark-area {
    left: 320px; top: 100px; width: 56px; height: 78px;
    background: var(--mark-tint-back);
  }
  .contact-name {
    position: absolute; left: 54px; top: 206px;
    font-size: 26px; font-weight: 700; color: var(--brand-green);
  }
  .contact-lines {
    position: absolute; left: 52px; top: 252px;
    font-size: 15.5px; line-height: 19.5px; color: var(--text-grey);
  }
  .contact-lines .address { margin-bottom: 7px; }
  .contact-lines .row { display: flex; align-items: center; gap: 7px; }
  .contact-lines svg { width: 13px; height: 13px; fill: var(--brand-green); flex: none; }
</style>
</head>
<body>
<div class="canvas">
  <section class="card card--front">
    <div class="wordmark"><span>Evergold</span><span>Fernbark INC</span></div>
    <div class="mark-area" role="img" aria-label="Brand tree mark area"></div>
    <div class="contact-name">Rovelio Marquin</div>
    <div class="contact-lines">
      <div class="address">284 Willowbend Creek Rd<br>Glenwood GA 30428</div>
      <div class="row">
        <svg viewBox="0 0 24 24" aria-hidden="true"><path d="M6.6 10.8a15.1 15.1 0 0 0 6.6 6.6l2.2-2.2a1 1 0 0 1 1-.25 11.4 11.4 0 0 0 3.6.57 1 1 0 0 1 1 1V20a1 1 0 0 1-1 1A17 17 0 0 1 3 4a1 1 0 0 1 1-1h3.5a1 1 0 0 1 1 1c0 1.25.2 2.45.57 3.57a1 1 0 0 1-.25 1z"/></svg>
        <span>912 555 0187</span>
      </div>
      <div class="row">
        <svg viewBox="0 0 24 24" aria-hidden="true"><path d="M2 5h20v14H2z M4 7v.5l8 5 8-5V7z" fill-rule="evenodd"/></svg>
        <span>evergoldfernbark@mailbrook.net</span>
      </div>
    </div>
  </section>
  <section class="card card--back">
    <div class="mark-area" role="img" aria-label="Brand tree mark area"></div>
    <div class="wordmark"><span>Evergold</span><span>Fernbark INC</span></div>
  </section>
</div>
</body>
</html>
```